手延うどん(乾麺)のパッケージデザイン(製品袋)を依頼させて頂きます。和紙系か和紙雲竜系の袋を考えていますので高級感のあるデザインを希望します。ターゲット層は40-60代の価格ではなく美味しさを求めているお客様。何本か並べると綺麗なデザイン。※現在販売しているデザインだと、シンプルすぎるかなと感じています。
サイズ:W50×D27×H25mm
参考に現在のデザイン写真を添付しておきます。
サイズが間違っていました。横50mm、縦270mm、厚み25mmです。
新たな写真を添付致しました。

和のイメージと背景の小麦のデザイン。温故知新も決め手のポイントでした。

今回、たくさんのデザイン案ありがとうございました。ヨツバリオさんを通してお願いしたのが初めてで、選ぶのに苦労しました・・・。次回もお願いしようと考えているので、機会がございましたら、またよろしくお願い致します。

```html
<!DOCTYPE html>
<html lang="ja">
<head>
<meta charset="utf-8">
<title>手延うどん パッケージ</title>
<link rel="stylesheet" href="https://fonts.googleapis.com/css2?family=Shippori+Mincho:wght@500;600&display=swap">
<style>
  :root {
    --backdrop: #a9c1b7;
    --washi: #f6f3ee;
    --washi-shade: #e9e4dc;
    --gold: #c9a24a;
    --gold-soft: #e3cf9c;
    --label: #2a201d;
  }
  html, body {
    margin: 0;
    padding: 0;
    width: 1200px;
    height: 2696px;
    overflow: hidden;
    background: var(--backdrop);
  }
  .canvas {
    position: relative;
    width: 1200px;
    height: 2696px;
  }
  .bag {
    position: absolute;
    left: 360px;
    top: 280px;
    width: 480px;
    height: 2220px;
    background: linear-gradient(90deg, var(--washi-shade) 0%, var(--washi) 18%, var(--washi) 82%, var(--washi-shade) 100%);
  }
  .noodle-pattern {
    position: absolute;
    inset: 0;
    background:
      radial-gradient(ellipse at 30% 20%, rgba(227,207,156,0.35), transparent 60%),
      radial-gradient(ellipse at 70% 60%, rgba(227,207,156,0.3), transparent 60%),
      radial-gradient(ellipse at 40% 90%, rgba(227,207,156,0.3), transparent 55%);
  }
  .label {
    position: absolute;
    left: 196px;
    top: 560px;
    width: 132px;
    height: 1000px;
    background: var(--label);
    display: flex;
    flex-direction: column;
    align-items: center;
  }
  .origin-badge {
    margin-top: 80px;
    width: 48px;
    height: 48px;
    border-radius: 50%;
    background: var(--gold);
    color: var(--label);
    font-family: "Shippori Mincho", serif;
    font-weight: 600;
    font-size: 18px;
    display: flex;
    align-items: center;
    justify-content: center;
    letter-spacing: 2px;
  }
  .product-name {
    margin: 64px 0 0;
    writing-mode: vertical-rl;
    font-family: "Shippori Mincho", serif;
    font-weight: 500;
    font-size: 80px;
    letter-spacing: 40px;
    color: var(--gold);
    line-height: 1;
  }
  .wheat-mark {
    position: absolute;
    left: 46px;
    top: 860px;
    width: 40px;
    height: 120px;
    border-radius: 20px 20px 4px 4px;
    background: linear-gradient(180deg, var(--gold-soft), var(--gold));
  }
</style>
</head>
<body>
  <main class="canvas">
    <section class="bag">
      <div class="noodle-pattern" role="img" aria-label="Flowing golden noodle-line pattern across the washi paper bag"></div>
      <div class="label">
        <div class="origin-badge">上州</div>
        <h1 class="product-name">手延うどん</h1>
        <div class="wheat-mark" role="img" aria-label="Gold wheat ear ornament"></div>
      </div>
    </section>
  </main>
</body>
</html>
```